Business Card Design - Crisp & Clean

Looking for a new clean and crisp business card design. Design must incorporate our corporate colors (see attached style sheet). We're a pretty fun loving group who likes to keep it light while still portraying a professional image. Card should incorporate both our logo and our mascot (see attachment). Card should be double sided and should have room for our social media - Facebook, Linked In and Twitter on the back. Font selections do not have to match the style guide.

```html
<!DOCTYPE html>
<html lang="en">
<head>
<meta charset="utf-8">
<title>Lumora HR – Business Card</title>
<link rel="stylesheet" href="https://fonts.googleapis.com/css2?family=Roboto+Condensed:wght@300;400;700&family=Roboto:wght@400;700;900&display=swap">
<style>
  :root {
    --brand-yellow: #fcc72c;
    --brand-yellow-soft: #fde58f;
    --ink: #141414;
    --paper: #ffffff;
    --stage: #2a2a2a;
    --mascot-base: #f3efe6;
  }
  * { box-sizing: border-box; margin: 0; padding: 0; }
  html, body { width: 1200px; height: 800px; overflow: hidden; }
  body {
    background: var(--stage);
    position: relative;
    font-family: "Roboto Condensed", sans-serif;
  }
  .card {
    position: absolute;
    top: 252px;
    width: 520px;
    height: 297px;
    background: var(--paper);
    overflow: hidden;
  }
  .card--front { left: 50px; }
  .card--back {
    left: 630px;
    border: 3px solid var(--brand-yellow);
    border-bottom-width: 9px;
  }

  /* Front */
  .front__panel { position: absolute; inset: 0; }
  .front__mascot {
    position: absolute;
    left: 14px; top: 10px;
    width: 180px; height: 277px;
    background: radial-gradient(circle at 50% 60%, var(--brand-yellow-soft) 0%, var(--mascot-base) 55%, var(--paper) 85%);
  }
  .front__identity {
    position: absolute;
    right: 26px; top: 46px;
    text-align: right;
    color: var(--paper);
  }
  .front__name { font-size: 23px; font-weight: 400; letter-spacing: 0.3px; }
  .front__title { font-size: 16px; font-weight: 300; margin-top: 2px; }
  .front__contact {
    position: absolute;
    right: 26px; bottom: 30px;
    text-align: right;
    color: var(--paper);
    font-size: 16px;
    font-weight: 300;
    line-height: 1.35;
  }

  /* Back */
  .back__content {
    position: absolute;
    inset: 0;
    display: flex;
    flex-direction: column;
    align-items: center;
    padding-top: 70px;
  }
  .brand-name {
    font-family: "Roboto", sans-serif;
    font-weight: 900;
    font-size: 52px;
    color: var(--ink);
    letter-spacing: -0.5px;
    line-height: 1;
  }
  .brand-tagline {
    font-family: "Roboto", sans-serif;
    font-weight: 700;
    font-size: 11.5px;
    color: var(--ink);
    letter-spacing: 0.4px;
    margin-top: 8px;
  }
  .social-list {
    list-style: none;
    margin-top: 34px;
    display: flex;
    flex-direction: column;
    gap: 10px;
  }
  .social-list__item {
    display: flex;
    align-items: center;
    gap: 10px;
    font-size: 15px;
    color: var(--ink);
  }
  .social-list__dot {
    width: 12px; height: 12px;
    border-radius: 50%;
    background: var(--brand-yellow);
  }
</style>
</head>
<body>

  <section class="card card--front" aria-label="Business card, front">
    <svg class="front__panel" width="520" height="297" viewBox="0 0 520 297" aria-hidden="true">
      <polygon fill="var(--brand-yellow)"
        points="208,0 520,0 520,297 208,297 208,176 226,158 208,140"/>
    </svg>
    <div class="front__mascot" role="img" aria-label="Space for the company mascot illustration"></div>
    <div class="front__identity">
      <p class="front__name">Maya Ellison</p>
      <p class="front__title">Marketing Wizard</p>
    </div>
    <div class="front__contact">
      <p>P: 555.014.2783</p>
      <p>E: maya@lumorahr.com</p>
      <p>lumorahr.com</p>
    </div>
  </section>

  <section class="card card--back" aria-label="Business card, back">
    <div class="back__content">
      <p class="brand-name">Lumora HR</p>
      <p class="brand-tagline">HR PROCESS MANAGEMENT SOLUTIONS</p>
      <ul class="social-list">
        <li class="social-list__item"><span class="social-list__dot"></span>itslumorahr</li>
        <li class="social-list__item"><span class="social-list__dot"></span>itslumorahr</li>
      </ul>
    </div>
  </section>

</body>
</html>
```